We need a business card design for an assisted living facility in Los Angeles. We have a logo selected but we would like a business card design that will leave a lasting impression on families looking to place their elderly loved ones in our care as well as on other facility providers who may refer their elderly residents to our facility.

```html
<!DOCTYPE html>
<html lang="en">
<head>
<meta charset="utf-8">
<title>Havenbrook Regal – Business Card</title>
<link rel="stylesheet" href="https://fonts.googleapis.com/css2?family=Cinzel:wght@400;500&family=Arimo:wght@400&display=swap">
<style>
  :root {
    --stage: #3c3c3c;
    --card-dark: #161616;
    --card-light: #ffffff;
    --brand-blue: #1565c0;
    --ink-gray: #555555;
    --rule-gray: #c9c9c9;
    --band-gray: #5a5a5a;
  }
  * { box-sizing: border-box; margin: 0; padding: 0; }
  html, body { width: 1200px; height: 689px; overflow: hidden; }
  body {
    background: var(--stage);
    display: flex;
    align-items: center;
    justify-content: center;
    gap: 56px;
  }
  .card {
    position: relative;
    width: 504px;
    height: 288px;
    border-radius: 18px;
    overflow: hidden;
  }
  .card--back {
    background: var(--card-dark);
    display: flex;
    align-items: center;
    justify-content: center;
  }
  .brand-name {
    font-family: "Cinzel", serif;
    font-weight: 400;
    color: var(--brand-blue);
    letter-spacing: 0.02em;
    white-space: nowrap;
  }
  .card--back .brand-name { font-size: 44px; }
  .brand-rule {
    display: block;
    height: 1px;
    background: #555;
    margin-top: 6px;
  }
  .card--front { background: var(--card-light); }
  .card--front .brand {
    position: absolute;
    top: 40px;
    right: 40px;
    text-align: right;
  }
  .card--front .brand-name { font-size: 26px; }
  .card--front .brand-rule { background: var(--rule-gray); }
  .address {
    position: absolute;
    top: 120px;
    right: 40px;
    text-align: right;
    font-family: "Arimo", sans-serif;
    font-size: 12px;
    line-height: 1.45;
    color: var(--ink-gray);
  }
  .divider {
    position: absolute;
    left: 40px;
    right: 40px;
    top: 186px;
    height: 1px;
    background: var(--rule-gray);
  }
  .person {
    position: absolute;
    left: 40px;
    top: 150px;
  }
  .person-name {
    font-family: "Cinzel", serif;
    font-weight: 500;
    font-size: 22px;
    color: var(--brand-blue);
    line-height: 1;
  }
  .person-title {
    font-family: "Arimo", sans-serif;
    font-size: 12px;
    color: var(--ink-gray);
    margin-top: 2px;
  }
  .contacts {
    position: absolute;
    left: 40px;
    top: 196px;
    list-style: none;
    font-family: "Arimo", sans-serif;
    font-size: 12px;
    color: var(--ink-gray);
  }
  .contacts li {
    display: flex;
    align-items: center;
    gap: 8px;
    line-height: 17px;
  }
  .contacts svg { width: 11px; height: 11px; fill: var(--brand-blue); }
  .footer-band {
    position: absolute;
    left: 0; right: 0; bottom: 0;
    height: 10px;
    display: flex;
  }
  .footer-band .band-blue { flex: 0 0 66%; background: var(--brand-blue); }
  .footer-band .band-gray { flex: 1; background: var(--band-gray); margin-left: 4px; }
</style>
</head>
<body>
  <section class="card card--back">
    <div class="brand">
      <span class="brand-name">Havenbrook Regal</span>
      <span class="brand-rule"></span>
    </div>
  </section>

  <section class="card card--front">
    <div class="brand">
      <span class="brand-name">Havenbrook Regal</span>
      <span class="brand-rule"></span>
    </div>

    <address class="address">
      4120 Willow Crest Road<br>
      Pasadena, California 91107<br>
      www.havenbrookliving.com
    </address>

    <div class="person">
      <p class="person-name">Daniel Reyes</p>
      <p class="person-title">President</p>
    </div>

    <div class="divider"></div>

    <ul class="contacts">
      <li>
        <svg viewBox="0 0 24 24" aria-hidden="true"><path d="M6.6 10.8a15 15 0 0 0 6.6 6.6l2.2-2.2c.3-.3.7-.4 1-.2 1.1.4 2.3.6 3.6.6.6 0 1 .4 1 1V20c0 .6-.4 1-1 1A17 17 0 0 1 3 4c0-.6.4-1 1-1h3.5c.6 0 1 .4 1 1 0 1.3.2 2.5.6 3.6.1.3 0 .7-.2 1z"/></svg>
        555-210-4817
      </li>
      <li>
        <svg viewBox="0 0 24 24" aria-hidden="true"><path d="M7 1h10a2 2 0 0 1 2 2v18a2 2 0 0 1-2 2H7a2 2 0 0 1-2-2V3a2 2 0 0 1 2-2zm0 3v15h10V4zm5 16a1 1 0 1 0 0 2 1 1 0 0 0 0-2z"/></svg>
        555-210-4922
      </li>
      <li>
        <svg viewBox="0 0 24 24" aria-hidden="true"><path d="M2 5h20v14H2zm2 2v.5l8 5 8-5V7zm0 3v7h16v-7l-8 5z"/></svg>
        info@havenbrook.com
      </li>
    </ul>

    <div class="footer-band">
      <span class="band-blue"></span>
      <span class="band-gray"></span>
    </div>
  </section>
</body>
</html>
```